Business Card for a recruitment agency specializing in engineers and geeks.

I am looking to create Business Card Design for my company.
That
## Company name:
Vornplick Inc.
Vornplick is a term coined from the following concepts.
1. geek + engineer
2. geek utopia
## Company Description:
The concept of the company is to be a recruitment agency that creates a paradise for geeky engineers. We want to be a place where engineers can have more freedom and ideal career support.
# Target.
The noun itself is often given to companies that want to hire engineers, geeks, and IT-related personnel, so it would be nice to get the impression that this company seems to have good engineers and IT personnel. There are many occasions where I meet with the human resources department, president, or senior management and give it to them.
# Atmosphere
We are happy with simplicity, but with an impact that will help people remember the company. The logo is based on a dinosaur that does programming, so it should be somewhat playful, but since it will basically be used in a business setting, please don't make it too silly.
# About the logo
See the attached files. The company logo represents our engineers smiling upward because of our work, with the motif of a dinosaur doing programming.
## Color
We will leave the color scheme to you, but since the logo is in black and white, colors with such a taste would fit well.
## file format
ai, psd, png, svg
Industry/Entity Type
human resource and employment agency
Contact Information for Business Card
Company name, address, email, tel, URL,logo
Colors
Designer to choose colors to be used in the design.
Look and feel
Each slider illustrates characteristics of the customer's brand and the style your logo design should communicate.

```html
<!DOCTYPE html>
<html lang="en">
<head>
<meta charset="utf-8">
<title>Vornplick Business Card</title>
<link href="https://fonts.googleapis.com/css2?family=Source+Sans+3:wght@400;600;700&display=swap" rel="stylesheet">
<style>
  :root {
    --bg: #e9eaea;
    --card-dark: #252525;
    --card-light: #f4f4f4;
    --ink: #2b2b2b;
    --ink-soft: #3a3a3a;
    --white: #ffffff;
    --pattern-light: #7a7a7a;
    --pattern-mid: #4a4a4a;
    --pattern-dark: #1c1c1c;
  }
  * { margin: 0; padding: 0; box-sizing: border-box; }
  html, body { width: 1200px; height: 960px; overflow: hidden; }
  body {
    background: var(--bg);
    position: relative;
    font-family: "Source Sans 3", "Source Sans Pro", Arial, sans-serif;
    color: var(--ink);
  }
  .card {
    position: absolute;
    left: 300px;
    width: 602px;
    height: 342px;
  }
  .card--front { top: 110px; background: var(--card-dark); overflow: hidden; }
  .card--back { top: 508px; background: var(--card-light); }

  .front-pattern {
    position: absolute;
    left: 0; top: 0; right: 0; bottom: 0;
    background:
      radial-gradient(ellipse 360px 300px at 12% 35%, rgba(122,122,122,0.75) 0%, rgba(74,74,74,0.45) 55%, rgba(28,28,28,0) 100%),
      linear-gradient(100deg, var(--pattern-mid) 0%, #363636 35%, #222222 60%, var(--pattern-dark) 100%);
  }
  .front-brand {
    position: absolute;
    left: 76px;
    top: 223px;
    display: flex;
    align-items: center;
    gap: 28px;
  }
  .front-brand__mark { width: 32px; height: 32px; background: var(--white); }
  .front-brand__name {
    font-size: 27px;
    font-weight: 600;
    color: var(--white);
    letter-spacing: 0.2px;
    line-height: 1;
  }

  .back-brand {
    position: absolute;
    left: 60px;
    top: 92px;
    width: 230px;
    display: flex;
    flex-direction: column;
    align-items: center;
    gap: 22px;
  }
  .back-brand__mark { width: 96px; height: 96px; background: var(--ink); }
  .back-brand__name {
    font-size: 38px;
    font-weight: 600;
    color: var(--ink);
    line-height: 1;
  }
  .divider {
    position: absolute;
    left: 299px;
    top: 85px;
    width: 2px;
    height: 172px;
    background: var(--ink);
  }
  .contact {
    position: absolute;
    left: 333px;
    top: 86px;
    font-size: 15px;
    line-height: 20px;
    color: var(--ink-soft);
  }
  .contact__name { font-size: 19px; font-weight: 700; color: var(--ink); line-height: 24px; }
  .contact__title { margin-bottom: 16px; }
  .contact__address { margin-bottom: 7px; }
  .contact__line { display: flex; align-items: center; gap: 5px; }
  .contact__line svg { width: 13px; height: 13px; flex: none; }
</style>
</head>
<body>
  <section class="card card--front">
    <div class="front-pattern" role="img" aria-label="Repeating grid of the brand symbol in tonal greys, lighter at left fading to black at right"></div>
    <div class="front-brand">
      <span class="front-brand__mark"></span>
      <span class="front-brand__name">Vornplick</span>
    </div>
  </section>

  <section class="card card--back">
    <div class="back-brand">
      <span class="back-brand__mark"></span>
      <span class="back-brand__name">Vornplick</span>
    </div>
    <div class="divider"></div>
    <div class="contact">
      <p class="contact__name">Daniel Harlow</p>
      <p class="contact__title">President</p>
      <p class="contact__address">48 N. W. 7th Street, Suite 115<br>Calder Bay, Ostrena, 40217</p>
      <p class="contact__line">
        <svg viewBox="0 0 16 16" aria-hidden="true"><path d="M3 1.5l3 .5 1 3.5-2 1.3a9 9 0 0 0 4.2 4.2l1.3-2 3.5 1 .5 3-2 1.5C7 14 2 9 1.5 3.5z" fill="none" stroke="#2b2b2b" stroke-width="1.5" stroke-linejoin="round"/></svg>
        (555) 014-2290
      </p>
      <p class="contact__line">
        <svg viewBox="0 0 16 16" aria-hidden="true"><rect x="1" y="3" width="14" height="10" fill="none" stroke="#2b2b2b" stroke-width="1.6"/><path d="M1 3l7 6 7-6" fill="none" stroke="#2b2b2b" stroke-width="1.6"/></svg>
        daniel@vornplick.com
      </p>
      <p class="contact__line">
        <svg viewBox="0 0 16 16" aria-hidden="true"><circle cx="8" cy="8" r="6.5" fill="none" stroke="#2b2b2b" stroke-width="1.5"/><ellipse cx="8" cy="8" rx="2.8" ry="6.5" fill="none" stroke="#2b2b2b" stroke-width="1.3"/><path d="M1.5 8h13" stroke="#2b2b2b" stroke-width="1.3"/></svg>
        www.vornplick.com
      </p>
    </div>
  </section>
</body>
</html>
```